Electrical Engineering Business Card Design

I need a business card design for an engineering consulting company based in Orlando, FL. I have had a logo created which the files are attached. We work primarily in the theme park and entertainment market sector but do projects in all market sectors. We have been serving Central Florida since 1994 and continue to strive to serve our clients and provide outstanding designs.
Industry/Entity Type
Theme Park

```html
<!DOCTYPE html>
<html lang="en">
<head>
<meta charset="utf-8">
<title>Brightmere Associates – Business Card</title>
<link rel="stylesheet" href="https://fonts.googleapis.com/css2?family=Montserrat:wght@400;600;700&display=swap">
<style>
  :root {
    --backdrop: #d9d6d1;
    --brand-green: #86b52a;
    --ink: #2b2b2b;
    --card-white: #f1f1f1;
    --text-grey: #4a4a4a;
    --card-w: 560px;
    --card-h: 320px;
  }
  * { box-sizing: border-box; margin: 0; padding: 0; }
  html, body {
    width: 1200px; height: 900px; overflow: hidden;
    background: var(--backdrop);
    font-family: "Montserrat", Arial, sans-serif;
  }
  .sheet {
    width: 1200px; height: 900px;
    display: flex; flex-direction: column;
    align-items: center; justify-content: center; gap: 60px;
  }
  .card {
    width: var(--card-w); height: var(--card-h);
    border-radius: 4px;
    box-shadow: 0 6px 18px rgba(0,0,0,0.18);
    position: relative;
  }
  .card--front {
    background: var(--brand-green);
    display: flex; align-items: center; justify-content: center;
  }
  .card--back { background: var(--card-white); }

  .brand { display: flex; align-items: center; gap: 14px; }
  .brand__square { width: 34px; height: 34px; background: var(--card-white); flex: none; }
  .brand__text { display: flex; flex-direction: column; }
  .brand__name {
    font-weight: 700; color: var(--ink); font-size: 30px; letter-spacing: 0.01em; line-height: 1.1;
  }
  .brand__place {
    font-weight: 700; color: var(--ink); font-size: 12px; letter-spacing: 0.34em; margin-top: 4px;
  }
  .card--back .brand { position: absolute; top: 34px; left: 50%; transform: translateX(-50%); }
  .card--back .brand__square { background: var(--brand-green); width: 26px; height: 26px; }
  .card--back .brand__name { font-size: 22px; }
  .card--back .brand__place { font-size: 9px; }

  .person {
    position: absolute; top: 118px; left: 0; right: 0; text-align: center;
    color: var(--brand-green); font-weight: 600; font-size: 19px;
  }
  .divider {
    position: absolute; top: 160px; left: 36px; right: 36px;
    height: 2px; background: var(--brand-green);
  }
  .contact {
    position: absolute; top: 188px; left: 44px;
    display: grid; grid-template-columns: 62px auto; row-gap: 8px;
    font-size: 13px; color: var(--text-grey);
  }
  .contact__label { color: var(--brand-green); font-weight: 700; }
  .address {
    position: absolute; top: 188px; right: 44px;
    font-size: 12px; color: var(--text-grey); line-height: 1.6;
  }
  .address__firm { font-weight: 700; color: var(--ink); }
</style>
</head>
<body>
<main class="sheet">
  <section class="card card--front" aria-label="Card front">
    <div class="brand">
      <span class="brand__square"></span>
      <div class="brand__text">
        <span class="brand__name">Brightmere Associates, P.A.</span>
        <span class="brand__place">ORLANDO, FLORIDA</span>
      </div>
    </div>
  </section>

  <section class="card card--back" aria-label="Card back">
    <div class="brand">
      <span class="brand__square"></span>
      <div class="brand__text">
        <span class="brand__name">Brightmere Associates, P.A.</span>
        <span class="brand__place">ORLANDO, FLORIDA</span>
      </div>
    </div>
    <p class="person">Dana Rell</p>
    <div class="divider"></div>
    <div class="contact">
      <span class="contact__label">PHONE</span><span>407-555-0148</span>
      <span class="contact__label">FAX</span><span>407-555-0193</span>
      <span class="contact__label">EMAIL</span><span>dana.rell@example.com</span>
    </div>
    <address class="address" style="font-style: normal;">
      <span class="address__firm">Brightmere Associates, PA</span><br>
      PO Box 410227<br>
      Orlando, FL 32801
    </address>
  </section>
</main>
</body>
</html>
```